Massage Therapy and Energy Healing Practice

I am a massage therapist, Reiki energy healer, I sell herbs and oils, and also a health lifestyle coach. I need a design that is strong because I'm not a spa. I do therapeutic work, but I want a touch of the energy and spiritual healing I do as well to be included in the design. I like blue, green, or purple colors. I live in the Blue Ridge Mountains of VA and even though my practice is in the city I like my love for nature and the earth to show through. I would like a single image logo so I can use the image many places. I need a strong brand that will let others know that I combine massage therapy in a therapeutic way while keeping my touches of energy healing, nurturing, herb crafting, and mother earth loving ways.
Updates

Just some things about me:I like to hike. I live on a farm. I own horses, cows, sheep and dogs. I love nature and the energy in produces. I'm very spiritual. I don't know how these things might help or if they do, but I know that my personality might help inspire what I will find good in a design. Added Sunday, December 13, 2015

Target Market(s)

People in pain. People who need spiritual council. Need herbal medicine advice. Holistic healthcare.

Industry/Entity Type

Massage

Contact Information for Business Card

Kneadwell Studio
Lorna T. Whitcombe C.M.T, R.M.T
40519 Hollin Creek Court, Tallowdale, VA
540-718-2437

Colors
3176b5
85abd2
876aae
9bcb3c

Requirements
Must have
• Strong Branding that promotes my massage therapy practice first
Nice to have
• Something to evoke my herbal medicine, my energy healing, my spiritual side

```html
<!DOCTYPE html>
<html lang="en">
<head>
<meta charset="utf-8">
<title>Kneadwell Studio – Business Card</title>
<link rel="stylesheet" href="https://fonts.googleapis.com/css2?family=Open+Sans:wght@400;600;700&display=swap">
<style>
  :root {
    --backdrop: #ecebe8;
    --card-white: #ffffff;
    --facet-grey: #ececec;
    --facet-soft: #f4f4f4;
    --charcoal: #2b2b2b;
    --charcoal-deep: #1f1f1f;
    --leaf-green: #8cc63f;
    --leaf-green-dark: #6fa52c;
    --ink: #3a3a3a;
    --text-light: #f2f2f2;
  }
  html, body {
    margin: 0;
    padding: 0;
    width: 1200px;
    height: 913px;
    overflow: hidden;
    background: var(--backdrop);
    font-family: "Open Sans", Arial, sans-serif;
  }
  .stage {
    width: 1200px;
    height: 913px;
    display: flex;
    align-items: center;
    justify-content: center;
  }
  .business-card {
    width: 900px;
    height: 514px;
    box-shadow: 0 18px 40px rgba(0,0,0,0.18);
    display: block;
  }
  .brand-name { font-family: "Open Sans", Arial, sans-serif; font-weight: 600; fill: var(--ink); }
  .holder-name { font-family: "Open Sans", Arial, sans-serif; font-weight: 700; fill: var(--card-white); }
  .credentials { font-family: "Open Sans", Arial, sans-serif; font-weight: 400; fill: var(--card-white); }
  .contact-text { font-family: "Open Sans", Arial, sans-serif; font-weight: 400; fill: var(--text-light); }
</style>
</head>
<body>
<main class="stage">
  <svg class="business-card" viewBox="0 0 900 514" xmlns="http://www.w3.org/2000/svg" aria-label="Kneadwell Studio business card">
    <!-- card base -->
    <rect class="card-base" width="900" height="514" fill="var(--card-white)"/>

    <!-- light facets in the white area -->
    <polygon class="facet-top-right" points="560,0 900,0 900,250 700,250" fill="var(--facet-grey)"/>
    <polygon class="facet-bottom-left" points="0,210 0,330 330,330 200,240" fill="var(--facet-soft)"/>
    <polygon class="facet-bottom-left-shade" points="0,250 0,330 250,330" fill="var(--facet-grey)"/>

    <!-- green edge above the dark band -->
    <polygon class="edge-stripe" points="0,322 330,322 330,336 0,336" fill="var(--leaf-green)"/>
    <polygon class="edge-stripe" points="650,250 900,236 900,250 650,264" fill="var(--leaf-green)"/>

    <!-- dark band -->
    <polygon class="dark-band" points="0,336 330,336 330,330 650,264 900,250 900,514 0,514" fill="var(--charcoal)"/>
    <polygon class="dark-band-shade" points="0,420 0,514 520,514" fill="var(--charcoal-deep)"/>

    <!-- name ribbon -->
    <polygon class="ribbon-fold" points="640,238 690,262 640,262" fill="var(--leaf-green-dark)"/>
    <polygon class="ribbon" points="290,300 640,238 660,300 330,360 310,350" fill="var(--leaf-green)"/>
    <polygon class="ribbon-fold" points="290,300 310,350 330,360 330,336" fill="var(--leaf-green-dark)"/>

    <!-- brand name -->
    <circle class="brand-dot" cx="300" cy="166" r="14" fill="var(--leaf-green)"/>
    <text class="brand-name" x="326" y="178" font-size="38">Kneadwell Studio</text>

    <!-- card holder -->
    <g transform="rotate(-10 470 300)">
      <text class="holder-name" x="470" y="306" font-size="27" text-anchor="middle">LORNA T. WHITCOMBE</text>
      <text class="credentials" x="560" y="326" font-size="13" text-anchor="middle">C.M.T, R.M.T</text>
    </g>

    <!-- divider -->
    <line class="divider" x1="560" y1="360" x2="600" y2="430" stroke="var(--leaf-green)" stroke-width="1.2"/>

    <!-- address -->
    <g class="contact-address">
      <circle cx="150" cy="400" r="20" fill="var(--leaf-green)"/>
      <path d="M150 388 a8 8 0 0 1 8 8 c0 6 -8 14 -8 14 s-8 -8 -8 -14 a8 8 0 0 1 8 -8z" fill="var(--card-white)"/>
      <circle cx="150" cy="396" r="3" fill="var(--leaf-green)"/>
      <text class="contact-text" x="60" y="470" font-size="15" transform="rotate(-18 60 470)">40519 Hollin Creek Court, Tallowdale, VA</text>
    </g>

    <!-- phone -->
    <g class="contact-phone">
      <circle cx="720" cy="320" r="20" fill="var(--leaf-green)"/>
      <path d="M709 316 q11 -8 22 0 l-2 4 q-9 -5 -18 0z" fill="var(--card-white)"/>
      <rect x="711" y="321" width="18" height="9" rx="2" fill="var(--card-white)"/>
      <text class="contact-text" x="710" y="372" font-size="14" transform="rotate(-18 710 372)">540-718-2437</text>
    </g>
  </svg>
</main>
</body>
</html>
```